Harborline Hound Fair Website Bright, colorful, hip

Expo website.
Harborline Hound Fair May 11th, 2019 from 11am-6pm
Brinley Commons, Baltimore MD
220 Exhibitors from NY to D.C.! Talks on BSL and Animal cruelty! Food Trucks! Live Music! On-Site Adoptions with T.O.W.L.s, Renowned Pitbull advocates Swingsets for Spaniels and Never Cage a Pup, Baltimore rescue Tails of Hope Oslo! Games! Contest! Kids Corner!

Target Market(s)

Pet Owners

Industry/Entity Type

Event

Number of Pages Required

2 page

Font styles to use
Sans Serif

Colors

Designer to choose colors to be used in the design.

Requirements
Must have
• Branded header. Slider with "features". Blog page. Google Map of Brinley Commons.
• "Want to be an exhibitor?!? Click here!"
Nice to have
• Bright and Bold. Super modern
Should not have
• White Space. Dont want to look like the other site I've done on this platform.

```html
<!DOCTYPE html>
<html lang="en">
<head>
<meta charset="utf-8">
<title>Harborline Hound Fair</title>
<link href="https://fonts.googleapis.com/css2?family=Roboto:wght@400;500;700;900&display=swap" rel="stylesheet">
<style>
:root{
  --teal:#5cc8ce;
  --teal-dark:#47b4ba;
  --ink:#4a4c52;
  --slate:#55585f;
  --bar:#4b4e55;
  --muted:#8a8d93;
  --ghost:#efefef;
  --white:#ffffff;
  --paper:#fafafa;
}
*{margin:0;padding:0;box-sizing:border-box}
html,body{width:1200px;height:3315px;overflow:hidden}
body{font-family:'Roboto',Arial,sans-serif;color:var(--ink);background:var(--white);position:relative}
.abs{position:absolute}
.pill{display:inline-flex;align-items:center;justify-content:space-between;border-radius:20px;font-size:10px;font-weight:700;text-transform:uppercase;letter-spacing:.4px}
.pill .chev{font-size:13px;font-weight:700}

/* top bar + header */
.topbar{left:0;top:0;width:1200px;height:27px;background:var(--bar)}
.social{top:7px;display:flex;gap:8px;left:773px}
.social span{width:13px;height:13px;background:#d8dadd;border-radius:2px;display:block}
.apply{left:941px;top:3px;width:93px;height:21px;background:var(--teal);color:var(--white);padding:0 12px;font-size:9px}
.header{left:0;top:27px;width:1200px;height:68px;background:var(--white);box-shadow:0 2px 6px rgba(0,0,0,.12);z-index:2}
.brand{left:166px;top:9px;display:flex;align-items:center;gap:10px}
.brand-dot{width:52px;height:52px;border-radius:50%;background:var(--teal)}
.brand-name{font-size:19px;font-weight:500;color:var(--teal);line-height:1.05;width:150px}
.nav{top:27px;font-size:11px;font-weight:500;text-transform:uppercase;color:var(--ink)}
.nav.active{color:var(--teal)}

/* hero */
.hero{left:0;top:95px;width:1200px;height:542px;background:linear-gradient(100deg,#8a6a3c 0%,#b08a52 30%,#9c8460 55%,#7f7563 80%,#a39173 100%)}
.hero-title{left:504px;top:272px;font-size:46px;font-weight:700;color:var(--white);text-transform:uppercase;letter-spacing:-.5px}
.hero-date{left:504px;top:330px;font-size:29px;font-weight:500;color:var(--white);text-transform:uppercase}
.hero-place{left:504px;top:366px;font-size:16px;font-weight:700;color:var(--white);text-transform:uppercase}
.hero-btn{left:504px;top:419px;width:161px;height:34px;background:var(--teal);color:var(--white);justify-content:center;font-size:9px}
.dots{left:979px;top:577px;display:flex;gap:6px}
.dots span{width:9px;height:9px;border-radius:50%;background:rgba(255,255,255,.6)}
.dots span:first-child{background:var(--teal)}

/* welcome */
.ghost-word{font-weight:900;color:var(--ghost);text-transform:uppercase;line-height:1;letter-spacing:4px}
.welcome-ghost{left:-8px;top:700px;font-size:118px}
.welcome-title{left:166px;top:740px;font-size:32px;font-weight:700;text-transform:uppercase}
.body-copy{font-size:11px;line-height:1.6;color:var(--muted)}
.welcome-copy{left:166px;top:822px;width:500px}
.welcome-copy p+p{margin-top:14px}
.welcome-copy b{color:var(--ink)}
.btn-dark{background:var(--slate);color:var(--white)}
.btn-light{background:var(--white);color:var(--ink)}
.btn-teal{background:var(--teal);color:var(--white)}
.welcome-btn{left:166px;top:983px;width:143px;height:36px;padding:0 20px}
.photo-round{border-radius:50%}

/* exhibitor band */
.band{left:0;top:1078px;width:1200px;height:535px;background:linear-gradient(180deg,#6dcbd0 0%,#5cc4c9 50%,#64c7cb 100%)}
.band-ghost{left:880px;top:1190px;font-size:118px;color:rgba(255,255,255,.12)}
.band-title{left:0;top:1142px;width:1200px;text-align:center;font-size:36px;font-weight:700;color:var(--white);text-transform:uppercase}
.band-copy{left:190px;top:1196px;width:820px;text-align:center;font-size:11px;line-height:1.6;color:rgba(255,255,255,.9)}
.card{top:1271px;width:266px}
.card-head{position:relative;height:80px}
.card-pill{position:absolute;left:40px;top:18px;width:226px;height:44px;background:var(--white);border-radius:22px;box-shadow:0 2px 6px rgba(0,0,0,.15);font-size:10px;color:var(--ink);padding-left:60px;display:flex;align-items:center}
.card-avatar{position:absolute;left:0;top:0;width:80px;height:80px;border-radius:50%;border:4px solid var(--white);box-shadow:0 2px 6px rgba(0,0,0,.15)}
.card h3{margin-top:22px;font-size:14px;font-weight:700;color:var(--white);line-height:1.3}
.card p{margin-top:14px;font-size:10px;line-height:1.55;color:rgba(255,255,255,.85)}
.card .pill{margin-top:22px;width:117px;height:32px;padding:0 16px}

/* exhibitors */
.ex-ghost{left:508px;top:1668px;font-size:112px}
.ex-kicker{left:166px;top:1676px;font-size:28px;font-weight:700;color:var(--teal);text-transform:uppercase}
.ex-title{left:166px;top:1702px;font-size:45px;font-weight:900;text-transform:uppercase;letter-spacing:-.5px}
.ex-copy{left:166px;top:1768px;width:870px}
.feature{top:1844px;width:260px;text-align:center}
.feature-icon{width:110px;height:110px;border-radius:50%;margin:0 auto;display:flex;align-items:center;justify-content:center}
.feature h4{margin-top:20px;font-size:15px;font-weight:700;text-transform:uppercase}
.feature p{margin-top:10px;font-size:10px;line-height:1.6;color:var(--muted)}
.feature .pill{margin-top:16px;width:117px;height:32px;padding:0 18px}

/* blog */
.blog{left:0;top:2188px;width:1200px;height:497px;background:var(--paper)}
.blog-ghost{left:-10px;top:2240px;font-size:118px}
.blog-title{left:0;top:2250px;width:1200px;text-align:center;font-size:38px;font-weight:700;text-transform:uppercase}
.blog-copy{left:230px;top:2306px;width:740px;text-align:center}
.post{top:2383px;height:234px;overflow:hidden}
.post-num{position:absolute;right:12px;top:8px;font-size:50px;font-weight:300;color:rgba(255,255,255,.45)}
.post-body{position:absolute;left:20px;bottom:18px;width:420px;color:var(--white)}
.post-body h5{font-size:20px;font-weight:700;text-transform:uppercase;white-space:nowrap}
.post-body small{display:block;font-size:8px;font-weight:700;text-transform:uppercase;margin-top:2px}
.post-body p{font-size:8px;line-height:1.5;margin-top:4px;opacity:.9}
.hover-note{left:412px;top:2624px;font-size:8px;color:var(--muted);text-transform:uppercase}

/* map */
.map{left:0;top:2685px;width:1200px;height:192px;background:linear-gradient(90deg,#e6e4df,#ecebe6 40%,#e3e6e3 70%,#e9e7e1)}

/* contact */
.contact{left:0;top:2877px;width:1200px;height:383px;background:var(--slate)}
.contact-title{left:0;top:2939px;width:1200px;text-align:center;font-size:32px;font-weight:700;color:var(--white);text-transform:uppercase}
.pin-circle{left:542px;top:3012px;width:110px;height:110px;border-radius:50%;background:var(--teal);display:flex;align-items:center;justify-content:center}
.contact-label{left:0;top:3138px;width:1200px;text-align:center;font-size:17px;font-weight:700;color:var(--teal);text-transform:uppercase}
.contact-place{left:0;top:3176px;width:1200px;text-align:center;font-size:12px;font-weight:500;color:var(--teal);text-transform:uppercase}

/* footer */
.footer{left:0;top:3260px;width:1200px;height:55px;background:var(--teal)}
.foot-link{top:3282px;font-size:9px;font-weight:500;color:var(--white);text-transform:uppercase}
.copyright{left:815px;top:3282px;width:219px;text-align:right;font-size:9px;color:var(--white);text-transform:uppercase}
</style>
</head>
<body>

<div class="abs topbar"></div>
<div class="abs social"><span></span><span></span><span></span><span></span></div>
<div class="abs pill apply">Apply Now <span class="chev">›</span></div>

<header class="abs header">
  <div class="abs brand"><span class="brand-dot"></span><span class="brand-name">Harborline Hound Fair</span></div>
  <span class="abs nav active" style="left:590px">Home</span>
  <span class="abs nav" style="left:656px">About</span>
  <span class="abs nav" style="left:731px">Location</span>
  <span class="abs nav" style="left:822px">Blog</span>
  <span class="abs nav" style="left:886px">Exhibitors</span>
  <span class="abs nav" style="left:988px">Contact</span>
</header>

<section class="abs hero" role="img" aria-label="Golden retriever running through dry golden grass"></section>
<h1 class="abs hero-title">Harborline Hound Fair</h1>
<p class="abs hero-date">May 11th, 2019 from 11am-6pm</p>
<p class="abs hero-place">Brinley Commons, Baltimore MD</p>
<div class="abs pill hero-btn">Add a dog event listing</div>
<div class="abs dots"><span></span><span></span><span></span><span></span></div>

<div class="abs ghost-word welcome-ghost">Welcome</div>
<h2 class="abs welcome-title">Harborline Hound Fair</h2>
<div class="abs body-copy welcome-copy">
  <p>Lorem ipsum dolor sit amet, <b>consectetur adipiscing elit.</b> Duis placerat dapibus urna, tempus lacinia diam viverra sit amet. Nam sed ullamcorper risus. Nulla dapibus nibh ut risus eleifend hendrerit. Vestibulum sodales eros tortor, vitae fringilla nisi fermentum.</p>
  <p>ante nec facilisis pulvinar, arcu augue finibus tortor, id commodo ante leo eu tellus. Aliquam varius pretium libero, vel amet eget dictum elit auctor a. Suspendisse scelerisque ornare iaculis. Fusce posuere sapien vel condimentum pulvinar. Sed pellentesque justo et est suscipit, ac aliquam nibh rhoncus. Maecenas volutpat risus ac justo feugiat pellentesque id non purus.</p>
</div>
<div class="abs pill btn-dark welcome-btn">Learn more <span class="chev">›</span></div>
<svg class="abs" style="left:696px;top:731px" width="292" height="292" viewBox="0 0 292 292" aria-hidden="true">
  <circle cx="146" cy="146" r="141" fill="none" stroke="#6a6d72" stroke-width="3" stroke-dasharray="0.1 9" stroke-linecap="round"/>
</svg>
<div class="abs photo-round" style="left:780px;top:762px;width:230px;height:230px;background:radial-gradient(circle at 50% 40%,#e9e3cf,#a9b77a 60%,#d6b63c)" role="img" aria-label="Golden retriever sitting in a meadow of wildflowers"></div>
<div class="abs photo-round" style="left:674px;top:805px;width:172px;height:172px;border:5px solid #fff;background:radial-gradient(circle at 45% 45%,#c98a4a,#8a5a2c 70%,#5b4a3a)" role="img" aria-label="Close-up of a golden dog"></div>

<section class="abs band" role="img" aria-label="Teal-tinted photo of a dog running across a field"></section>
<div class="abs ghost-word band-ghost">Event</div>
<h2 class="abs band-title">Want to be an exhibitor ?</h2>
<p class="abs band-copy">Quisque pharetra finibus urna, in commodo augue iaculis ac. Etiam metus leo, venenatis sagittis auctor ac, vestibulum quis urna. Nam turpis metus, eleifend in mauris sed, tincidunt tempor nunc. Aenean feugiat dignissim ex, vel sollicitudin.</p>

<article class="abs card" style="left:166px">
  <div class="card-head"><div class="card-pill">1st September, 2018 (Saturday)</div><div class="card-avatar" style="background:linear-gradient(135deg,#e2c49a,#9b6a3a)" role="img" aria-label="Beagle portrait"></div></div>
  <h3>Etiam metus leo, venenatis sagittis auctor ac vestibulum quis urna</h3>
  <p>Quisque pharetra finibus urna, in commodo augue iaculis ac. Etiam metus leo, venenatis sagittis auctor ac, vestibulum quis urna Nam turpis...</p>
  <div class="pill btn-light">Click here <span class="chev">›</span></div>
</article>
<article class="abs card" style="left:466px">
  <div class="card-head"><div class="card-pill">1st September, 2018 (Saturday)</div><div class="card-avatar" style="background:linear-gradient(135deg,#c78b56,#6f4a2b)" role="img" aria-label="Brown dog portrait"></div></div>
  <h3>Etiam metus leo, venenatis sagittis auctor ac vestibulum quis urna</h3>
  <p>Quisque pharetra finibus urna, in commodo augue iaculis ac. Etiam metus leo, venenatis sagittis auctor ac, vestibulum quis urna Nam turpis...</p>
  <div class="pill btn-dark">Click here <span class="chev">›</span></div>
</article>
<article class="abs card" style="left:767px">
  <div class="card-head"><div class="card-pill">1st September, 2018 (Saturday)</div><div class="card-avatar" style="background:linear-gradient(135deg,#f4efe6,#c9b79c)" role="img" aria-label="White terrier portrait"></div></div>
  <h3>Etiam metus leo, venenatis sagittis auctor ac vestibulum quis urna</h3>
  <p>Quisque pharetra finibus urna, in commodo augue iaculis ac. Etiam metus leo, venenatis sagittis auctor ac, vestibulum quis urna Nam turpis...</p>
  <div class="pill btn-dark">Click here <span class="chev">›</span></div>
</article>

<div class="abs ghost-word ex-ghost">Exhibitors</div>
<p class="abs ex-kicker">220 Exhibitors</p>
<h2 class="abs ex-title">From NY to D.C.</h2>
<p class="abs body-copy ex-copy">Quisque pharetra finibus urna, in commodo augue iaculis ac. Etiam metus leo, venenatis sagittis auctor ac, vestibulum quis urna. Nam turpis metus, eleifend in mauris sed, tincidunt tempor nunc. Aenean feugiat dignissim ex, vel sollicitudin.</p>

<div class="abs feature" style="left:164px">
  <div class="feature-icon" style="background:var(--slate)"><svg width="48" height="44" viewBox="0 0 24 22"><path d="M12 21 2.5 11.5A5.5 5.5 0 0 1 12 4a5.5 5.5 0 0 1 9.5 7.5Z" fill="#fff"/></svg></div>
  <h4>Animal Cruelty</h4>
  <p>Quisque pharetra finibus urna, in commodo augue iaculis ac. Etiam metus leo, venenatis sagittis auctor ac, vestibulum quis urna. Nam turpis metus, eleifend in mauris sed.</p>
  <div class="pill btn-dark" style="margin-left:72px">Learn more <span class="chev">›</span></div>
</div>
<div class="abs feature" style="left:467px">
  <div class="feature-icon" style="background:var(--teal)"><svg width="44" height="48" viewBox="0 0 22 24"><path d="M8 18V4l12-3v14" fill="none" stroke="#fff" stroke-width="2"/><circle cx="5" cy="18" r="3.5" fill="#fff"/><circle cx="17" cy="15" r="3.5" fill="#fff"/></svg></div>
  <h4>Live Music</h4>
  <p>Quisque pharetra finibus urna, in commodo augue iaculis ac. Etiam metus leo, venenatis sagittis auctor ac, vestibulum quis urna. Nam turpis metus, eleifend in mauris sed.</p>
  <div class="pill btn-teal" style="margin-left:72px">Learn more <span class="chev">›</span></div>
</div>
<div class="abs feature" style="left:772px">
  <div class="feature-icon" style="background:var(--teal)"><svg width="50" height="40" viewBox="0 0 25 20"><path d="M2 8h21l-2 10H4Z" fill="#fff"/><path d="M5 8a7.5 6 0 0 1 15 0" fill="none" stroke="#fff" stroke-width="2"/></svg></div>
  <h4>Food Trucks</h4>
  <p>Quisque pharetra finibus urna, in commodo augue iaculis ac. Etiam metus leo, venenatis sagittis auctor ac, vestibulum quis urna. Nam turpis metus, eleifend in mauris sed.</p>
  <div class="pill btn-teal" style="margin-left:72px">Learn more <span class="chev">›</span></div>
</div>

<section class="abs blog"></section>
<div class="abs ghost-word blog-ghost">Blog</div>
<h2 class="abs blog-title">Latest Post</h2>
<p class="abs body-copy blog-copy">Quisque pharetra finibus urna, in commodo augue iaculis ac. Etiam metus leo, venenatis sagittis auctor ac, vestibulum quis urna. Nam turpis metus, eleifend in mauris sed, tincidunt tempor nunc. Aenean feugiat dignissim ex, vel sollicitudin.</p>

<article class="abs post" style="left:164px;width:450px">
  <div style="position:absolute;inset:0;background:linear-gradient(120deg,#6b5a48,#3c3430 60%,#554a40)" role="img" aria-label="Two dogs sitting together"></div>
  <div style="position:absolute;inset:0;background:rgba(60,62,68,.35)"></div>
  <span class="post-num">01</span>
  <div class="post-body"><h5>Nulla in dapibus justo</h5><small>Posted on 1st September, 2018</small><p>Nulla odio leo, maximus in condimentum at, maximus ac amet lacus. Fusce dictum mi eget luke efficitur ullamcorper nam blandit Nulla odio leo, maximus at condimentum at, maximus sit amet lacus maximus.</p></div>
</article>
<article class="abs post" style="left:621px;width:131px">
  <div style="position:absolute;inset:0;background:linear-gradient(160deg,#b59a86,#7a5f50)" role="img" aria-label="Dog resting its head"></div>
  <span class="post-num" style="font-size:40px">02</span>
  <div class="post-body" style="left:8px"><h5>Nulla in dapibus</h5><small>Posted on 1st Septem</small><p>Nulla odio leo, maximus<br>luke efficitur ullamcorper<br>nam blandit Nulla odio leo</p></div>
</article>
<article class="abs post" style="left:760px;width:135px">
  <div style="position:absolute;inset:0;background:linear-gradient(160deg,#7d7c5a,#3f3a2e)" role="img" aria-label="Smiling dog outdoors"></div>
  <span class="post-num" style="font-size:40px">03</span>
  <div class="post-body" style="left:8px"><h5>Nulla in dapibus</h5><small>Posted on 1st Septem</small><p>Nulla odio leo, maximus<br>luke efficitur ullamcorper<br>nam blandit Nulla odio leo</p></div>
</article>
<article class="abs post" style="left:902px;width:132px">
  <div style="position:absolute;inset:0;background:linear-gradient(160deg,#a18a66,#5e4c36)" role="img" aria-label="Dog in a sunny field"></div>
  <span class="post-num" style="font-size:40px">04</span>
  <div class="post-body" style="left:8px"><h5>Nulla in dapibus</h5><small>Posted on 1st Septem</small><p>Nulla odio leo, maximus<br>luke efficitur ullamcorper<br>nam blandit Nulla odio leo</p></div>
</article>
<p class="abs hover-note">On mouse hover</p>

<section class="abs map" role="img" aria-label="Street map of Brinley Commons, Baltimore"></section>

<section class="abs contact"></section>
<h2 class="abs contact-title">Contact Details</h2>
<div class="abs pin-circle"><svg width="30" height="42" viewBox="0 0 20 28"><path d="M10 1a9 9 0 0 0-9 9c0 7 9 17 9 17s9-10 9-17a9 9 0 0 0-9-9Z" fill="#fff"/><circle cx="10" cy="10" r="3.5" fill="var(--teal)"/></svg></div>
<p class="abs contact-label">Location</p>
<p class="abs contact-place">Brinley Commons, Baltimore MD</p>

<footer class="abs footer"></footer>
<span class="abs foot-link" style="left:166px">Home</span>
<span class="abs foot-link" style="left:216px">About</span>
<span class="abs foot-link" style="left:281px">Location</span>
<span class="abs foot-link" style="left:358px">Blog</span>
<span class="abs foot-link" style="left:408px">Exhibitors</span>
<span class="abs foot-link" style="left:497px">Contact</span>
<span class="abs copyright">Copyright@2018. All right reserved</span>

</body>
</html>
```